Design Bramwell Precast Core Values

We are a precast concrete manufacturing company that is looking to present (and eventually include in marketing) our core values to our employees (and eventually our customers). These values represent the morals, motivation and mission of our company. It is important to use these statements for evaluating performance and communicating who we are to both potential new-hires as well as new contractors.
Please design a graphic, hopefully using a product (or similar storm drain picture) image to organize the following:
BRAMWELL PRECAST CORE VALUES
1. We are committed to one another
• Coaching culture
• LMA (lead, manage, accountability)
• Employees win
• Zero 4 Ever
2. We know what our customers need
• Extensive experience
• Value engineering
• Excellent communication
3. We go the extra “yard”
• Follow up, follow through
• “Can do” attitude
• Do the little things well (Do the ordinary extraordinarily)

```html
<!DOCTYPE html>
<html lang="en">
<head>
<meta charset="utf-8">
<title>Bramwell Precast Core Values</title>
<link href="https://fonts.googleapis.com/css2?family=Anton&family=Archivo+Black&family=Archivo:wght@400&display=swap" rel="stylesheet">
<style>
  :root {
    --yellow: #f8d30f;
    --black: #000000;
    --white: #ffffff;
    --frame: #1a1a1a;
  }
  html, body {
    margin: 0;
    padding: 0;
    width: 1200px;
    height: 1200px;
    overflow: hidden;
    background: var(--white);
  }
  .canvas {
    position: relative;
    width: 1200px;
    height: 1200px;
  }
  .values-card {
    position: absolute;
    left: 368px;
    top: 120px;
    width: 416px;
    height: 940px;
    border: 1px solid var(--frame);
    box-sizing: border-box;
    background: var(--white);
    overflow: hidden;
  }
  .card-bg {
    position: absolute;
    left: 0;
    top: 0;
  }
  .card-title {
    position: absolute;
    left: 0;
    top: 25px;
    width: 100%;
    margin: 0;
    text-align: center;
    font-family: "Anton", "Oswald", sans-serif;
    font-weight: 400;
    font-size: 31px;
    line-height: 31px;
    letter-spacing: 0.5px;
    color: var(--black);
  }
  .value-number {
    position: absolute;
    left: 188px;
    width: 40px;
    height: 40px;
    border-radius: 50%;
    background: var(--yellow);
    color: var(--black);
    font-family: "Anton", sans-serif;
    font-size: 25px;
    line-height: 40px;
    text-align: center;
  }
  .value-line {
    position: absolute;
    left: 0;
    width: 100%;
    margin: 0;
    text-align: center;
    color: var(--white);
    font-family: "Archivo Black", "Arial Black", sans-serif;
    font-size: 12.5px;
    line-height: 16px;
    transform: translateY(-8px);
    letter-spacing: 0.2px;
  }
  .value-line .light,
  .value-line.light {
    font-family: "Archivo", Arial, sans-serif;
    font-weight: 400;
  }
  .brand-mark {
    position: absolute;
    display: flex;
    align-items: center;
    gap: 6px;
    font-family: "Archivo Black", "Arial Black", sans-serif;
    font-size: 14px;
    color: var(--black);
  }
  .brand-mark .square {
    width: 16px;
    height: 16px;
    background: var(--black);
  }
  .brand-mark .circle {
    width: 18px;
    height: 18px;
    border-radius: 50%;
    background: var(--yellow);
  }
</style>
</head>
<body>
<div class="canvas">
  <section class="values-card">
    <svg class="card-bg" width="416" height="940" viewBox="0 0 416 940" aria-hidden="true">
      <rect x="0" y="0" width="416" height="802" fill="var(--black)"/>
      <polygon points="0,0 416,0 416,97.6 208,112 0,97.6" fill="var(--yellow)"/>
    </svg>

    <h1 class="card-title">BRAMWELL PRECAST<br>CORE VALUES</h1>

    <div class="value-number" style="top:141.6px">3</div>
    <p class="value-line" style="top:204px">We are committed to one another</p>
    <p class="value-line" style="top:236px">Coaching culture</p>
    <p class="value-line" style="top:268.8px">LMA <span class="light">(lead, manage, accountability)</span></p>
    <p class="value-line" style="top:300.8px">Employees win</p>
    <p class="value-line" style="top:332.8px">Zero 4 Ever</p>

    <div class="value-number" style="top:370.4px">3</div>
    <p class="value-line" style="top:432.8px">We know what our customers need</p>
    <p class="value-line" style="top:464.8px">Extensive experience</p>
    <p class="value-line" style="top:497.6px">Value engineering</p>
    <p class="value-line" style="top:529.6px">Excellent communication</p>

    <div class="value-number" style="top:568.8px">3</div>
    <p class="value-line" style="top:628px">We go the extra “yard”</p>
    <p class="value-line" style="top:660px">Follow up, follow through</p>
    <p class="value-line" style="top:692.8px">“Can do” attitude</p>
    <p class="value-line" style="top:724.8px">Do the little things well</p>
    <p class="value-line light" style="top:757.6px">(Do the ordinary extraordinarily)</p>

    <div class="brand-mark" style="left:40px; top:860px">
      <span class="square"></span>Bramwell Precast
    </div>
    <div class="brand-mark" style="left:240px; top:860px">
      <span class="circle"></span>Bramwell Precast
    </div>
  </section>
</div>
</body>
</html>
```